Home Security check flyer

I am a locksmith company. Wanting a flyer designed for postal delivery to houses.
The design is to have a home security check list similar to the one attached (Not exactly the same) targeting locks with some pictures of deadlocks, Deadbolts, Window Locks, Security door locks Etc..
The idea is to get people in there homes to make sure they are secure and if not to call us for a free quote.
Flyer is to catch customers eye so they don't just throw it our. E.G. IS YOUR HOME SECURE on the front
A4 Size to be folded to twice to envelope size.
My company information can be found at
www.brightvalekeyworks.com.au

Reason: Want to try a few changes on some of the eliminated ones.

Target Market(s)

residential homes (Security)

Industry/Entity Type

Locksmith

Requirements
Must have
• My logo and contact information
Based on information from www.brightvalekeyworks.com.au

```html
<!DOCTYPE html>
<html lang="en">
<head>
<meta charset="utf-8">
<title>Home Security Audit – Brightvale Keyworks</title>
<link href="https://fonts.googleapis.com/css2?family=Roboto+Slab:wght@300;400;700&family=Arimo:wght@400;700&display=swap" rel="stylesheet">
<style>
:root{
  --page-dark:#2b2b2b;
  --page-dark-edge:#0f0f0f;
  --page-light:#ffffff;
  --strip:#585858;
  --trim:#6b4fa0;
  --brand-red:#d0262b;
  --ink:#1d1d1d;
  --ink-soft:#555555;
  --box:#3a3a3a;
}
*{margin:0;padding:0;box-sizing:border-box}
html,body{width:1200px;height:821px;overflow:hidden;background:#ffffff}
.canvas{position:relative;width:1200px;height:821px;background:#ffffff}

/* ---------- cover page ---------- */
.cover{
  position:absolute;left:30px;top:44px;width:566px;height:737px;
  background:radial-gradient(ellipse at 55% 35%,#4a4a4a 0%,var(--page-dark) 45%,var(--page-dark-edge) 100%);
  border:1px solid var(--trim);
  color:#ffffff;font-family:"Roboto Slab",serif;
}
.brand-box{
  position:absolute;left:64px;top:6px;width:182px;height:77px;background:#ffffff;
  display:flex;flex-direction:column;align-items:center;justify-content:center;gap:3px;
}
.brand-name{color:var(--brand-red);font-weight:700;font-size:21px;line-height:1;text-transform:uppercase;letter-spacing:.5px;text-align:center}
.brand-line{color:var(--brand-red);font-weight:700;font-size:10px;line-height:1;text-align:center}
.cover-title{position:absolute;left:50px;top:110px;font-weight:300;font-size:28px;line-height:1.1}
.cover-copy{position:absolute;left:50px;top:143px;width:500px;font-weight:300;font-size:14.5px;line-height:1.4}
.cover-copy p+p{margin-top:10px}
.cover-web{position:absolute;left:50px;top:300px;font-weight:300;font-size:19px;line-height:1.2}
.cover-call{position:absolute;left:50px;top:322px;font-weight:300;font-size:22px;line-height:1.2}
.cover-art{
  position:absolute;left:52px;top:370px;width:498px;height:366px;
  background:radial-gradient(ellipse at 55% 55%,#8f8f8f 0%,#5a5a5a 45%,rgba(30,30,30,0) 75%);
}

/* ---------- checklist page ---------- */
.checklist{
  position:absolute;left:596px;top:44px;width:590px;height:737px;
  background:var(--page-light);border:1px solid var(--trim);border-left:none;
  font-family:"Arimo",sans-serif;color:var(--ink);
}
.side-strip{position:absolute;right:0;top:0;width:207px;height:100%;background:var(--strip)}
.side-photo{position:absolute;left:406px;width:101px;border:2px solid #ffffff}
.photo-remote{top:314px;height:117px;background:linear-gradient(135deg,#c9ccd0,#6f757c 60%,#3b3f44)}
.photo-dial{top:452px;height:111px;background:radial-gradient(circle at 50% 50%,#dfe3e8,#7e8894 55%,#2f3a48)}
.photo-keypad{top:574px;height:106px;background:linear-gradient(160deg,#f2f2f2,#b9bcc0 55%,#7c7f84)}

.section-title{font-weight:700;font-size:10.5px;line-height:1.2;color:var(--ink)}
.rows{position:absolute;left:24px;width:350px;display:flex;flex-direction:column;justify-content:space-between}
.rows-other{top:48px;height:158px}
.rows-home{top:409px;height:326px}
.row{display:grid;grid-template-columns:82px 74px 1fr;align-items:center}
.row-label{font-size:8.5px;line-height:1.1;color:var(--ink)}
.row-note{font-size:4.8px;line-height:1.15;color:var(--ink-soft)}
.yn{display:flex;gap:8px;font-size:7.5px;align-items:center}
.yn span{display:inline-flex;align-items:center;gap:2px}
.yn span::after{content:"";display:inline-block;width:8px;height:8px;border:1px solid var(--box)}

.personal{position:absolute;left:24px;top:221px;width:350px}
.question{position:relative;margin-top:12px;padding-right:58px}
.question h3{font-weight:700;font-size:8.3px;line-height:1.2}
.question p{font-size:5.2px;line-height:1.25;color:var(--ink-soft);margin-top:1px}
.question .yn{position:absolute;right:0;top:0}
.badge{position:absolute;left:300px;top:166px;width:28px;height:28px;border-radius:50%;background:#2b2b2b}
</style>
</head>
<body>
<div class="canvas">

  <section class="cover">
    <div class="brand-box">
      <div class="brand-name">Brightvale Keyworks</div>
      <div class="brand-line">Keys and locks, day and night</div>
    </div>
    <h1 class="cover-title">Home Security Audit</h1>
    <div class="cover-copy">
      <p>House-breaking is one of the most common crimes and can occur at any time of the day or night. This checklist is designed to help you take a fresh look at your home security.</p>
      <p>You can take steps to reduce identified risk areas in your home and reduce the likelihood of becoming a victim of crime or a repeat victim of crime. How does your home security rate?</p>
    </div>
    <div class="cover-web">www.safehomes.gov.au</div>
    <div class="cover-call">Call us today 03 9012 4478</div>
    <div class="cover-art" role="img" aria-label="Illustration of a two-storey house with a ring of house keys in front"></div>
  </section>

  <section class="checklist">
    <div class="side-strip"></div>
    <div class="side-photo photo-remote" role="img" aria-label="Photo of a hand holding a car remote key"></div>
    <div class="side-photo photo-dial" role="img" aria-label="Photo of a safe combination dial"></div>
    <div class="side-photo photo-keypad" role="img" aria-label="Photo of a digital keypad door lock"></div>

    <h2 class="section-title" style="position:absolute;left:24px;top:34px">Other safety considerations</h2>
    <div class="rows rows-other">
      <div class="row"><span class="row-label">Clear vision?</span><span class="yn"><span>Y</span><span>N</span></span><span class="row-note">Make sure doors and windows can be seen clearly from outside</span></div>
      <div class="row"><span class="row-label">Trees/shrubs trimmed?</span><span class="yn"><span>Y</span><span>N</span></span><span class="row-note">Trim plants that hide doors and windows from passers-by</span></div>
      <div class="row"><span class="row-label">Garage/shed secure?</span><span class="yn"><span>Y</span><span>N</span></span><span class="row-note">Keep garages and sheds locked at all times</span></div>
      <div class="row"><span class="row-label">Tools secure?</span><span class="yn"><span>Y</span><span>N</span></span><span class="row-note">Lock tools away so they cannot be used to get in</span></div>
      <div class="row"><span class="row-label">Wheelie bins secured?</span><span class="yn"><span>Y</span><span>N</span></span><span class="row-note">Store bins where they cannot be used to climb fences</span></div>
      <div class="row"><span class="row-label">Gates to yard secured?</span><span class="yn"><span>Y</span><span>N</span></span><span class="row-note">Lock side gates with a sturdy padlock</span></div>
      <div class="row"><span class="row-label">Meter box secured?</span><span class="yn"><span>Y</span><span>N</span></span><span class="row-note">Fit an approved lock to your meter box</span></div>
      <div class="row"><span class="row-label">House numbers?</span><span class="yn"><span>Y</span><span>N</span></span><span class="row-note">House numbers should be clearly visible from the street</span></div>
      <div class="row"><span class="row-label">Smoke alarms?</span><span class="yn"><span>Y</span><span>N</span></span><span class="row-note">Install smoke alarms and plan a fire escape route</span></div>
      <div class="row"><span class="row-label">Security alarms?</span><span class="yn"><span>Y</span><span>N</span></span><span class="row-note">Monitored alarms deter intruders from entering your home</span></div>
      <div class="row"><span class="row-label">Safe disposal of personal documents?</span><span class="yn"><span>Y</span><span>N</span></span><span class="row-note">Shred papers that show your name, address or account details</span></div>
    </div>

    <div class="personal">
      <h2 class="section-title">Personal Security in the Home</h2>
      <div class="question">
        <h3>Do you keep information about your security arrangements private?</h3>
        <p>Be careful of sharing details of your home security with people you do not know, and avoid posting them online.</p>
        <span class="yn"><span>Y</span><span>N</span></span>
      </div>
      <div class="question">
        <h3>Do you keep information about your personal arrangements private?</h3>
        <p>Information about holidays and daily routines should be kept private and shared only with people you trust.</p>
        <span class="yn"><span>Y</span><span>N</span></span>
      </div>
      <div class="question">
        <h3>Do you store valuables out of sight and reach from outside?</h3>
        <p>Keep valuables out of view from windows and doors, and store spare keys in a secure place.</p>
        <span class="yn"><span>Y</span><span>N</span></span>
      </div>
      <div class="question">
        <h3>Do you have important phone numbers stored in your phone?</h3>
        <p>Keep emergency numbers close to your phone so help can be called quickly if an incident occurs.</p>
        <span class="yn"><span>Y</span><span>N</span></span>
      </div>
      <div class="badge"></div>
    </div>

    <div class="rows rows-home">
      <h2 class="section-title">Security Doors</h2>
      <div class="row"><span class="row-label">All entry points?</span><span class="yn"><span>Y</span><span>N</span></span><span class="row-note">Security doors deter intruders from entering your home</span></div>
      <div class="row"><span class="row-label">Firm joints?</span><span class="yn"><span>Y</span><span>N</span></span><span class="row-note">Check joints and hinges are solid and secure</span></div>
      <div class="row"><span class="row-label">Triple locks?</span><span class="yn"><span>Y</span><span>N</span></span><span class="row-note">Triple locks increase the strength of your doors</span></div>
      <h2 class="section-title">Main Entry/Exit Doors</h2>
      <div class="row"><span class="row-label">Front - solid core?</span><span class="yn"><span>Y</span><span>N</span></span><span class="row-note">Solid doors resist forced entry far better</span></div>
      <div class="row"><span class="row-label">Front - viewer?</span><span class="yn"><span>Y</span><span>N</span></span><span class="row-note">A viewer lets you see callers before opening</span></div>
      <div class="row"><span class="row-label">Back - solid core?</span><span class="yn"><span>Y</span><span>N</span></span><span class="row-note">Back doors should be solid and well fitted</span></div>
      <div class="row"><span class="row-label">Adequate locks?</span><span class="yn"><span>Y</span><span>N</span></span><span class="row-note">Deadlocks are the best choice for entry doors</span></div>
      <div class="row"><span class="row-label">Keyed alike?</span><span class="yn"><span>Y</span><span>N</span></span><span class="row-note">One key for all doors saves time and effort</span></div>
      <h2 class="section-title">Sliding Doors</h2>
      <div class="row"><span class="row-label">Patio bolts?</span><span class="yn"><span>Y</span><span>N</span></span><span class="row-note">Patio bolts stop sliding doors being lifted out</span></div>
      <h2 class="section-title">Windows</h2>
      <div class="row"><span class="row-label">Key operated locks?</span><span class="yn"><span>Y</span><span>N</span></span><span class="row-note">Key operated locks add strength to every window</span></div>
      <div class="row"><span class="row-label">Keyed alike?</span><span class="yn"><span>Y</span><span>N</span></span><span class="row-note">Keyed alike locks make daily use simple</span></div>
      <div class="row"><span class="row-label">Security screens?</span><span class="yn"><span>Y</span><span>N</span></span><span class="row-note">Screens and grilles let air in and keep others out</span></div>
      <div class="row"><span class="row-label">Warning stickers?</span><span class="yn"><span>Y</span><span>N</span></span><span class="row-note">Warning stickers may deter intruders from trying</span></div>
      <h2 class="section-title">Lighting</h2>
      <div class="row"><span class="row-label">Main entry/exits?</span><span class="yn"><span>Y</span><span>N</span></span><span class="row-note">Light all main entry points to your home</span></div>
      <div class="row"><span class="row-label">Timers fitted?</span><span class="yn"><span>Y</span><span>N</span></span><span class="row-note">Timers turn lights on while you are away</span></div>
      <div class="row"><span class="row-label">Timers used?</span><span class="yn"><span>Y</span><span>N</span></span><span class="row-note">Set timers to match your usual evening routine</span></div>
      <div class="row"><span class="row-label">Sensor lighting?</span><span class="yn"><span>Y</span><span>N</span></span><span class="row-note">Sensor lights startle anyone moving near the house</span></div>
      <h2 class="section-title">Property Marking</h2>
      <div class="row"><span class="row-label">Engraved with code?</span><span class="yn"><span>Y</span><span>N</span></span><span class="row-note">Engrave valuables with your licence number</span></div>
      <div class="row"><span class="row-label">Photos recorded?</span><span class="yn"><span>Y</span><span>N</span></span><span class="row-note">Photograph items and keep the images safe</span></div>
      <div class="row"><span class="row-label">Inventory list?</span><span class="yn"><span>Y</span><span>N</span></span><span class="row-note">Keep a list of serial numbers and models</span></div>
    </div>
  </section>

</div>
</body>
</html>
```